Design a label for a range of honey under :BRIGHT MEADOW HONEY. (Original quirky different)

Create a label for a range of honey products under the brand BRIGHT MEADOW HONEY.
Iam the beekeeper and want to sell for the local New Zealand market directly to the consumer, online mainly.
Brand position: A contemporary honey, a fresh look for a simple product, like nature intended, nothing taken out, nothing added. Doesnt take itself seriously.
Personality: Contemporary, fresh, modern, free and fun,loving. Doesnt take itself seriously, loving, generous, upbeat, provide enjoyment, life ...
Brand value: Straight up, keep it simple, generous, different,
Label: Modern twist of nature and goodness (no straight picture of nature) quirky?, use of slogan? ( Nature in a pot / More than just honey / Taste of nature / It's all good...
Need to stand out, make you smile, be noticed, different...

Target Market(s)

Online direct customer.

Requirements
Must have
• legal requirements for NZ labeling attached.
A twist and quirky side...
Should not have
• Basic picture of nature.
Straight forward boring everybody else's feel.

```html
<!DOCTYPE html>
<html lang="en">
<head>
<meta charset="utf-8">
<title>Bright Meadow Honey – Label Range</title>
<link href="https://fonts.googleapis.com/css2?family=Sniglet:wght@400;800&display=swap" rel="stylesheet">
<style>
  :root {
    --ink: #231f20;
    --paper: #ffffff;
    --natural: #c07a14;
    --raspberry: #c8104a;
    --cocoa: #5e2e06;
    --sky: #62c9ee;
    --weight-text: #6b3a4a;
  }
  html, body {
    margin: 0;
    padding: 0;
    width: 1200px;
    height: 1200px;
    overflow: hidden;
    background: var(--paper);
    font-family: "Sniglet", cursive;
  }
  .canvas {
    position: relative;
    width: 1200px;
    height: 1200px;
  }
  .label {
    position: absolute;
    display: block;
  }
  .label--natural   { left: 108px; top: 200px; width: 316px; height: 287px; }
  .label--raspberry { left: 108px; top: 508px; width: 316px; height: 287px; }
  .label--cocoa     { left: 108px; top: 814px; width: 316px; height: 287px; }
  .label--feature   { left: 704px; top: 722px; width: 350px; height: 318px; }

  .label__name {
    font-family: "Sniglet", cursive;
    font-weight: 800;
    fill: var(--ink);
    text-anchor: middle;
    letter-spacing: 0.5px;
  }
  .label__flavour {
    font-family: "Sniglet", cursive;
    font-weight: 800;
    fill: var(--paper);
    text-anchor: middle;
    letter-spacing: 0.5px;
  }
  .label__weight {
    font-family: "Sniglet", cursive;
    font-weight: 800;
    fill: var(--weight-text);
    text-anchor: middle;
  }

  .brand-mark {
    position: absolute;
    left: 690px;
    top: 70px;
    width: 380px;
    text-align: center;
  }
  .brand-mark__dot {
    display: block;
    width: 130px;
    height: 130px;
    margin: 20px auto 46px;
    border-radius: 50%;
    background: var(--natural);
  }
  .brand-mark__name {
    margin: 0;
    font-family: "Sniglet", cursive;
    font-weight: 800;
    font-size: 84px;
    line-height: 0.95;
    color: var(--ink);
    letter-spacing: 1px;
  }
</style>
</head>
<body>
<main class="canvas">

  <svg width="0" height="0" aria-hidden="true" style="position:absolute">
    <defs>
      <path id="hex-shape" d="M 90,5 L 230,5 Q 250,5 259,23 L 306,127 Q 315,145 306,163 L 259,267 Q 250,285 230,285 L 90,285 Q 70,285 61,267 L 14,163 Q 5,145 14,127 L 61,23 Q 70,5 90,5 Z"/>
      <clipPath id="hex-clip"><use href="#hex-shape"/></clipPath>
    </defs>
  </svg>

  <!-- Natural -->
  <svg class="label label--natural" viewBox="0 0 320 290">
    <use href="#hex-shape" fill="var(--paper)"/>
    <circle cx="160" cy="62" r="28" fill="var(--natural)"/>
    <text class="label__name" x="160" y="146" font-size="42">BRIGHT</text>
    <text class="label__name" x="160" y="183" font-size="36">MEADOW</text>
    <text class="label__name" x="160" y="210" font-size="24">HONEY</text>
    <g clip-path="url(#hex-clip)">
      <rect x="0" y="220" width="320" height="32" fill="var(--natural)"/>
    </g>
    <use href="#hex-shape" fill="none" stroke="var(--ink)" stroke-width="7"/>
    <text class="label__flavour" x="160" y="243" font-size="22">natural</text>
    <text class="label__weight" x="160" y="272" font-size="10">500g</text>
  </svg>

  <!-- Raspberry -->
  <svg class="label label--raspberry" viewBox="0 0 320 290">
    <use href="#hex-shape" fill="var(--paper)"/>
    <circle cx="160" cy="62" r="28" fill="var(--raspberry)"/>
    <text class="label__name" x="160" y="146" font-size="42">BRIGHT</text>
    <text class="label__name" x="160" y="183" font-size="36">MEADOW</text>
    <text class="label__name" x="160" y="210" font-size="24">HONEY</text>
    <g clip-path="url(#hex-clip)">
      <rect x="0" y="220" width="320" height="32" fill="var(--raspberry)"/>
    </g>
    <use href="#hex-shape" fill="none" stroke="var(--ink)" stroke-width="7"/>
    <text class="label__flavour" x="160" y="243" font-size="22">raspberry</text>
    <text class="label__weight" x="160" y="272" font-size="10">500g</text>
  </svg>

  <!-- Cocoa -->
  <svg class="label label--cocoa" viewBox="0 0 320 290">
    <use href="#hex-shape" fill="var(--paper)"/>
    <circle cx="160" cy="62" r="28" fill="var(--cocoa)"/>
    <text class="label__name" x="160" y="146" font-size="42">BRIGHT</text>
    <text class="label__name" x="160" y="183" font-size="36">MEADOW</text>
    <text class="label__name" x="160" y="210" font-size="24">HONEY</text>
    <g clip-path="url(#hex-clip)">
      <rect x="0" y="220" width="320" height="32" fill="var(--cocoa)"/>
    </g>
    <use href="#hex-shape" fill="none" stroke="var(--ink)" stroke-width="7"/>
    <text class="label__flavour" x="160" y="243" font-size="22">cocoa</text>
    <text class="label__weight" x="160" y="272" font-size="10">500g</text>
  </svg>

  <!-- Brand mark -->
  <div class="brand-mark">
    <span class="brand-mark__dot" aria-hidden="true"></span>
    <p class="brand-mark__name">BRIGHT<br>MEADOW<br>HONEY</p>
  </div>

  <!-- Featured natural label, flat -->
  <svg class="label label--feature" viewBox="0 0 320 290">
    <use href="#hex-shape" fill="var(--paper)"/>
    <circle cx="160" cy="62" r="28" fill="var(--natural)"/>
    <text class="label__name" x="160" y="146" font-size="42">BRIGHT</text>
    <text class="label__name" x="160" y="183" font-size="36">MEADOW</text>
    <text class="label__name" x="160" y="210" font-size="24">HONEY</text>
    <g clip-path="url(#hex-clip)">
      <rect x="0" y="220" width="320" height="32" fill="var(--natural)"/>
    </g>
    <use href="#hex-shape" fill="none" stroke="var(--ink)" stroke-width="6"/>
    <text class="label__flavour" x="160" y="243" font-size="22">natural</text>
    <text class="label__weight" x="160" y="272" font-size="10">500g</text>
  </svg>

</main>
</body>
</html>
```